Law firm Seeks Modern and Engaging Site Redesign

Law firm seeks a new web site. Should be modern, but retaining existing logo. Needs to include contact section, professional bio, services offered, and contact information.

The site should be modern, responsive, and able to be SEO optimized.

The finished product should be coded in a Wordpress site, which I will provide. I can work with other platforms, including Wix, but WP is preferred.

Note the current site is https://www.tallowfieldlaw.example/#/home

Target Market(s)

Family Law Practice

Industry/Entity Type

Legal

Coding

Coded - Design and coding required

Number of Pages Required

4 page

Font styles to use
Sans Serif

Requirements
Must have
• Service description
Bio pages for partners
Contact Form
Awards/Publication page

```html
<!DOCTYPE html>
<html lang="en">
<head>
<meta charset="utf-8">
<title>Tallowfield Marsh Attorneys at Law</title>
<link rel="stylesheet" href="https://fonts.googleapis.com/css2?family=Fira+Sans:wght@400;500;600;700&family=Lato:wght@400;700&display=swap">
<style>
:root{
  --blue:#3d64d8;
  --blue-deep:#1336a6;
  --ink:#222;
  --text:#333;
  --grey-logo:#6b7280;
  --dark-band:#2a2a2a;
  --light-band:#dcdcdc;
  --white:#fff;
  --line:#9aa0ac;
}
*{margin:0;padding:0;box-sizing:border-box}
html,body{width:1200px;height:3981px;overflow:hidden;background:var(--white)}
body{position:relative;font-family:"Lato",sans-serif;color:var(--text)}
.abs{position:absolute}
.heading{font-family:"Fira Sans",sans-serif;font-weight:700;letter-spacing:.5px}
.btn{position:absolute;display:flex;align-items:center;justify-content:center;background:var(--blue);color:var(--white);border-radius:24px;font-family:"Fira Sans",sans-serif;font-size:17px}
.underline{position:absolute;height:5px;width:78px;background:var(--blue);left:561px}

/* header */
.brand{position:absolute;left:97px;top:30px;color:var(--grey-logo);font-family:"Fira Sans",sans-serif;font-weight:400}
.brand .name{font-size:38px;line-height:1}
.brand .tag{font-size:15px;margin-top:4px;padding-left:172px}
.nav{position:absolute;top:54px;left:530px;display:flex;gap:32px;font-family:"Fira Sans",sans-serif;font-weight:500;font-size:16px;color:var(--ink)}

/* hero */
.hero-img{position:absolute;left:99px;top:124px;width:1101px;height:552px;background:linear-gradient(100deg,#3a2e22 0%,#6f5a44 40%,#a88a63 60%,#4a3a29 100%)}
.hero-text{position:absolute;left:183px;top:270px;color:var(--white)}
.hero-text .welcome{font-family:"Fira Sans",sans-serif;font-size:46px;font-weight:400}
.hero-text .big{font-family:"Fira Sans",sans-serif;font-size:43px;font-weight:700;line-height:54px}
.dots span{position:absolute;left:1086px;width:15px;height:15px;border:2px solid var(--white);border-radius:50%}
.thumbs{position:absolute;left:773px;top:611px;width:390px;height:133px;background:var(--white);padding:9px 9px;display:flex;gap:9px}
.thumbs div{flex:1;height:123px}

/* about */
.who{position:absolute;left:99px;top:794px;display:flex;align-items:center;gap:18px;font-family:"Fira Sans",sans-serif;font-size:20px;color:var(--ink)}
.who i{display:block;width:50px;height:3px;background:var(--blue)}
.about-title{position:absolute;left:97px;top:826px;font-size:44px;color:var(--blue)}
.about-copy{position:absolute;left:99px;top:895px;width:502px;font-size:13.5px;line-height:20px;text-align:justify}
.about-copy p+p{margin-top:18px}
.about-frame{position:absolute;left:657px;top:836px;width:459px;height:337px;border:3px solid var(--blue)}
.about-photo{position:absolute;left:642px;top:821px;width:459px;height:338px;background:linear-gradient(90deg,#b9bcc0,#dfe1e4 50%,#a7aaae)}

/* services */
.services{position:absolute;left:0;top:1263px;width:1200px;height:538px;background:linear-gradient(180deg,#cfcfcf,#f1f1f1 50%,#d6d6d6)}
.section-title{position:absolute;width:1200px;text-align:center;font-size:42px}
.card{position:absolute;top:1442px;width:474px;height:268px;background:var(--white);box-shadow:0 0 6px rgba(0,0,0,.15)}
.card .inner{position:absolute;inset:8px;border:1px solid #ddd}
.card h3{position:absolute;top:90px;width:100%;text-align:center;font-family:"Fira Sans",sans-serif;font-weight:600;font-size:23px;color:var(--blue)}
.card p{position:absolute;top:122px;left:42px;right:42px;text-align:center;font-size:13px;line-height:18px}
.card .more{position:absolute;left:187px;top:207px;width:102px;height:31px;border:1px solid var(--ink);display:flex;align-items:center;justify-content:center;font-family:"Fira Sans",sans-serif;font-weight:600;font-size:12px;color:var(--ink)}
.badge{position:absolute;width:130px;height:130px;border-radius:50%;background:var(--blue);border:6px solid #b9c5ec}

/* team */
.team{position:absolute;left:0;top:1800px;width:1200px;height:712px;background:var(--dark-band)}
.member{position:absolute;top:1976px;width:340px;text-align:center;color:var(--white)}
.member .photo{width:228px;height:228px;border-radius:50%;border:4px solid #ddd;margin:0 auto}
.member h4{margin-top:30px;font-family:"Fira Sans",sans-serif;font-weight:600;font-size:23px}
.member p{margin:10px auto 0;width:300px;font-size:10.5px;line-height:16px}
.member .btn{position:relative;margin:26px auto 0;width:157px;height:45px}

/* directions */
.map{position:absolute;left:99px;top:2693px;width:475px;height:444px;background:linear-gradient(135deg,#e8ede6,#dde7dc 55%,#a9c9ef 70%,#e6ebe4)}
.field{position:absolute;left:626px;width:475px;height:50px;border:1.5px solid var(--line);padding:0 20px;display:flex;align-items:center;font-family:"Fira Sans",sans-serif;font-weight:600;font-size:16px;color:var(--ink)}

/* cta */
.cta{position:absolute;left:0;top:3205px;width:1200px;height:329px;background:var(--blue-deep)}
.cta-text{position:absolute;left:99px;top:3296px;width:620px;color:var(--white);font-size:28px;line-height:37px}
.cta-art{position:absolute;left:690px;top:3226px;width:468px;height:308px;background:linear-gradient(160deg,#5a78d4,#3352b8)}

/* footer */
.foot-brand{position:absolute;left:0;width:1200px;top:3572px;text-align:center;color:var(--grey-logo);font-family:"Fira Sans",sans-serif}
.foot-brand .name{font-size:36px}
.foot-brand .tag{font-size:14px;margin-top:2px}
.foot-icons{position:absolute;top:3653px;left:531px;display:flex;gap:14px}
.foot-icons span{width:36px;height:36px;border:2px solid var(--blue);border-radius:50%;display:flex;align-items:center;justify-content:center}
.address{position:absolute;top:3702px;width:1200px;text-align:center;font-size:16px;line-height:21.5px;color:var(--ink)}
.listing{position:absolute;left:512px;top:3806px;width:173px;height:78px;border:2px solid #ccc;background:#fafafa}
.listing i{position:absolute;left:0;right:0;bottom:0;height:20px;background:#f07b1c}
.rule{position:absolute;left:0;top:3915px;width:1200px;height:1px;background:#ddd}
.copy{position:absolute;top:3937px;width:1200px;text-align:center;font-size:12px;color:var(--ink)}
</style>
</head>
<body>

<header>
  <div class="brand"><div class="name">Tallowfield Marsh</div><div class="tag">Attorneys at Law</div></div>
  <nav class="nav"><span>HOME</span><span>FAMILY LAW</span><span>CRIMINAL LAW</span><span>ABOUT</span><span>CONTACT</span></nav>
  <svg class="abs" style="left:1078px;top:56px" width="22" height="22" viewBox="0 0 22 22" fill="none" stroke="#3d64d8" stroke-width="2"><circle cx="9" cy="9" r="7"/><path d="M14 14l6 6"/></svg>
</header>

<section class="hero">
  <div class="hero-img" role="img" aria-label="Courthouse columns with scales of justice on a law book"></div>
  <div class="hero-text">
    <div class="welcome">Welcome to</div>
    <div class="big">TALLOWFIELD | MARSH</div>
    <div class="big">ATTORNEYS AT LAW</div>
  </div>
  <div class="btn" style="left:181px;top:459px;width:157px;height:45px">Read More</div>
  <div class="dots"><span style="top:320px"></span><span style="top:344px;background:radial-gradient(circle,#fff 35%,transparent 40%)"></span><span style="top:369px"></span></div>
  <svg class="abs" style="left:580px;top:658px" width="38" height="38" viewBox="0 0 38 38"><circle cx="19" cy="19" r="18" fill="#fff"/><circle cx="19" cy="19" r="11" fill="none" stroke="#333" stroke-width="1.8"/><path d="M14 17l5 5 5-5" fill="none" stroke="#333" stroke-width="1.8"/></svg>
  <div class="thumbs">
    <div role="img" aria-label="Gavel on wooden block" style="background:linear-gradient(135deg,#3b2a15,#b88a3e)"></div>
    <div role="img" aria-label="Statue of justice against blue sky" style="background:linear-gradient(135deg,#3d6ab8,#c9d3e6)"></div>
    <div role="img" aria-label="Gavel in warm light" style="background:linear-gradient(135deg,#e07a25,#7a2e0e)"></div>
  </div>
</section>

<section class="about">
  <div class="who"><i></i>Who We Are</div>
  <h1 class="about-title heading">TALLOWFIELD MARSH, LLC</h1>
  <div class="about-copy">
    <p>The law firm of Tallowfield Marsh, LLC is based in Millbrook County, conveniently located in Millbrook, New Jersey at 18 Harbor Commons. We serve the needs of clients throughout Millbrook County, as well as, clients from several other counties, including, but not limited to, the surrounding northern counties. Between our partners, we have over 30+ years of experience assisting clients with all of their family law and criminal law needs.</p>
    <p>Often times the areas of family law and criminal law cross paths, which can be both emotionally and financially complex. We understand that our client’s case is unique and pride ourselves on being responsive to all of our clients needs.</p>
  </div>
  <div class="btn" style="left:99px;top:1119px;width:157px;height:45px">Read More</div>
  <div class="about-frame"></div>
  <div class="about-photo" role="img" aria-label="The two founding partners standing in the firm's office lobby"></div>
</section>

<section>
  <div class="services"></div>
  <h2 class="section-title heading" style="top:1312px;color:var(--ink)">SERVICES OFFERED</h2>
  <div class="underline" style="top:1376px"></div>

  <div class="card" style="left:99px"><div class="inner"></div>
    <h3>FAMILY LAW</h3>
    <p>Lorem Ipsum is simply dummy text of the printing and typesetting industry. Lorem Ipsum has been the industry's standard dummy text ever since the 1500s, when an unknown printer took a galley of type and scrambled.</p>
    <div class="more">READ MORE</div>
  </div>
  <div class="badge" style="left:274px;top:1388px"></div>
  <svg class="abs" style="left:306px;top:1422px" width="66" height="62" viewBox="0 0 66 62" fill="none" stroke="#fff" stroke-width="2.4"><circle cx="20" cy="12" r="7"/><circle cx="46" cy="12" r="7"/><circle cx="33" cy="30" r="5"/><path d="M8 58V34q0-10 12-10t12 10M34 58V34q0-10 12-10t12 10M27 58V44q0-6 6-6t6 6v14"/></svg>

  <div class="card" style="left:625px"><div class="inner"></div>
    <h3>CRIMINAL LAW</h3>
    <p>Lorem Ipsum is simply dummy text of the printing and typesetting industry. Lorem Ipsum has been the industry's standard dummy text ever since the 1500s, when an unknown printer took a galley of type and scrambled.</p>
    <div class="more">READ MORE</div>
  </div>
  <div class="badge" style="left:798px;top:1388px"></div>
  <svg class="abs" style="left:823px;top:1428px" width="80" height="50" viewBox="0 0 80 50" fill="none" stroke="#fff" stroke-width="2.6"><circle cx="22" cy="28" r="16"/><circle cx="22" cy="28" r="9"/><circle cx="56" cy="28" r="16"/><circle cx="56" cy="28" r="9"/><path d="M34 14q5-10 10 0"/></svg>
</section>

<section>
  <div class="team"></div>
  <h2 class="section-title heading" style="top:1866px;color:var(--white)">OUR TEAM</h2>
  <div class="underline" style="top:1930px"></div>
  <svg class="abs" style="left:44px;top:2046px" width="44" height="90" viewBox="0 0 44 90" fill="none" stroke="#bbb" stroke-width="2.5"><path d="M42 2L2 45l40 43"/></svg>
  <svg class="abs" style="left:1102px;top:2046px" width="44" height="90" viewBox="0 0 44 90" fill="none" stroke="#bbb" stroke-width="2.5"><path d="M2 2l40 43L2 88"/></svg>

  <div class="member" style="left:77px">
    <div class="photo" role="img" aria-label="Portrait of Daniel R. Tallowfield" style="background:linear-gradient(180deg,#d7d4cf,#4a5060)"></div>
    <h4>DANIEL R. TALLOWFIELD</h4>
    <p>Daniel R. Tallowfield practices in the area of family law, specializing in high conflict matters relating to divorce, custody, equitable distribution and complex financial issues. He also handles related litigation and defense matters, as well as domestic violence proceedings.</p>
    <div class="btn">Read More</div>
  </div>
  <div class="member" style="left:431px">
    <div class="photo" role="img" aria-label="Portrait of Owen P. Marsh" style="background:linear-gradient(180deg,#7a6e66,#1f2228)"></div>
    <h4>OWEN P. MARSH</h4>
    <p>Owen P. Marsh is one of the founding partners of the firm. His primary concentration is in the areas of matrimonial, family law, appellate work, juvenile delinquency, criminal and municipal court, residential real estate transactions and wills and estates.</p>
    <div class="btn">Read More</div>
  </div>
  <div class="member" style="left:779px">
    <div class="photo" role="img" aria-label="Portrait of Laura M. Ashby" style="background:linear-gradient(180deg,#b08a78,#2b2626)"></div>
    <h4>LAURA M. ASHBY</h4>
    <p>Laura M. Ashby has been an associate at Tallowfield Marsh since 2016. In private practice, she focuses on family and divorce law, including child custody, child and spousal support and equitable distribution. She is a member of the Millbrook County Bar Association.</p>
    <div class="btn">Read More</div>
  </div>
</section>

<section>
  <h2 class="section-title heading" style="top:2570px;color:var(--ink)">HOW TO GET HERE</h2>
  <div class="underline" style="top:2634px"></div>
  <div class="map" role="img" aria-label="Street map showing the office location beside the river"></div>
  <div class="field" style="top:2693px">NAME</div>
  <div class="field" style="top:2753px">EMAIL</div>
  <div class="field" style="top:2813px">PHONE</div>
  <div class="field" style="top:2874px;justify-content:space-between">PRACTICE AREA<svg width="12" height="9" viewBox="0 0 12 9"><path d="M0 0h12L6 9z" fill="#222"/></svg></div>
  <div class="field" style="top:2937px;height:137px;align-items:flex-start;padding-top:14px">MESSAGE</div>
  <div class="btn" style="left:627px;top:3095px;width:157px;height:45px">Submit</div>
  <div class="btn" style="left:797px;top:3095px;width:157px;height:45px">Reset</div>
</section>

<section>
  <div class="cta"></div>
  <p class="cta-text heading">TO DISCUSS YOUR MATTER WITH EITHER MR. TALLOWFIELD OR MR. MARSH SEND US YOUR DETAILS ABOUT YOUR SITUATION OR CONTACT US DIRECTLY AT (555) 014-2200.</p>
  <div class="cta-art" role="img" aria-label="Courthouse and quill pen illustration"></div>
</section>

<footer>
  <div class="foot-brand"><div class="name">Tallowfield Marsh</div><div class="tag">Attorneys at Law</div></div>
  <div class="foot-icons">
    <span><svg width="16" height="18" viewBox="0 0 16 18" fill="none" stroke="#3d64d8" stroke-width="1.8"><path d="M8 17s6-6 6-10A6 6 0 0 0 2 7c0 4 6 10 6 10z"/><circle cx="8" cy="7" r="2"/></svg></span>
    <span><svg width="18" height="18" viewBox="0 0 18 18" fill="none" stroke="#3d64d8" stroke-width="1.8"><path d="M4 1l3 4-2 2q2 4 6 6l2-2 4 3-2 3Q6 16 1 4z"/></svg></span>
    <span><svg width="18" height="16" viewBox="0 0 18 16" fill="none" stroke="#3d64d8" stroke-width="1.8"><rect x="4" y="1" width="10" height="4"/><rect x="1" y="5" width="16" height="7"/><rect x="4" y="10" width="10" height="5"/></svg></span>
  </div>
  <div class="address">18 Harbor Commons Drive Suite 310<br>Millbrook, NJ 07000<br>(555) 014-2200 | (555) 014-2201<br><strong>Tallowfield &amp; Marsh, LLC</strong></div>
  <div class="listing"><i></i></div>
  <div class="rule"></div>
  <div class="copy">Tallowfield | Marsh Attorneys at Law | Copyright © 2020</div>
</footer>

</body>
</html>
```